Neuroscience laboratory website

The "Speech, Thought and Nerve Lab" (aka, SoTeN Lab) is looking for a web site design. We are a cognitive neuroscience of language laboratory, which means we study the brain circuits involved in language comprehension. We need a professional-looking web presence where we can introduce the kind of research we do, list our publications, present our research team, present the current experiments that are being conducted and present our lab blog. Our current web site is displayed at http://soten-lab.example-host.io/soten.lab.example-host.io/. The new design should be a net improvement over the existing one.
Updates

Project Deadline Extended
Reason: Error was made when posting the contest. I am rectifying it now.

Target Market(s)

Primary audience will be other academics and university-age students interested in learning more about the lab, but it should also target the general adult public based in western countries.

Industry/Entity Type

Laboratory

Colors

Designer to choose colors to be used in the design.

Requirements
Nice to have
• It would be nice if the design could be informed by at least one of all the following concepts: Human languages/scripts, mind, brain, neuroimaging and brain signals (like electroencephalogram), neuroscience, science, knowledge.

Word or visual play with the acronym of the lab (SoTeN) would be permissable, if a good idea can be extracted out of it.
Should not have
• Design should have a clean background. It should use large framing images very sparingly, if at all.

```html
<!DOCTYPE html>
<html lang="en">
<head>
<meta charset="utf-8">
<title>Speech, Thought and Nerve Lab</title>
<link rel="stylesheet" href="https://fonts.googleapis.com/css2?family=PT+Sans+Narrow:wght@400;700&family=Source+Sans+3:wght@300;400;600&display=swap">
<style>
:root{
  --header-bg:#333333;
  --footer-bg:#3a3a3a;
  --teal:#2bb5b3;
  --teal-dark:#1f9c9a;
  --text:#555555;
  --heading:#3a3a3a;
  --panel:#e1e1e1;
  --white:#ffffff;
  --social-1:#4a6fb5;
  --social-2:#4bc0e8;
  --social-3:#e55a5a;
}
*{margin:0;padding:0;box-sizing:border-box}
html,body{width:1040px;height:1200px;overflow:hidden;background:var(--white)}
body{position:relative;font-family:"Source Sans 3",sans-serif;color:var(--text)}
.abs{position:absolute}

/* header */
.site-header{position:absolute;left:0;top:0;width:1040px;height:92px;background:var(--header-bg)}
.brand{position:absolute;left:112px;top:55px;font-size:14px;color:var(--white);font-weight:400}
.nav{position:absolute;top:36px;left:0;height:36px}
.nav a{position:absolute;top:0;height:36px;line-height:36px;color:#e8e8e8;font-size:16.5px;font-weight:300;text-decoration:none;white-space:nowrap}
.nav a.active{background:linear-gradient(var(--teal),var(--teal-dark));color:var(--white);border-radius:3px;width:70px;text-align:center}

/* hero */
.hero{position:absolute;left:0;top:92px;width:1040px;height:392px;
  background:radial-gradient(ellipse at 35% 45%,#3fb0e0 0%,#1565b5 35%,#0a2a66 70%,#061a3f 100%)}
.welcome{position:absolute;left:578px;top:97px;width:355px;height:190px;background:rgba(40,52,70,.72);padding:16px 16px 0 16px;color:var(--white)}
.welcome h1{font-weight:300;font-size:31px;letter-spacing:.3px;line-height:1}
.welcome p{margin-top:12px;font-size:13px;font-weight:300;line-height:15.6px}
.btn{position:absolute;left:16px;top:133px;width:105px;height:34px;line-height:34px;text-align:center;background:linear-gradient(var(--teal),var(--teal-dark));color:var(--white);font-size:16px;border-radius:3px}
.slider-nav{position:absolute;left:119px;top:339px;width:50px;height:35px;background:rgba(20,35,60,.75)}
.hero-tag{position:absolute;left:731px;top:359px;font-size:14px;font-weight:300;color:#b8c6d6}

/* content */
h2.big{font-weight:300;font-size:31px;color:var(--heading);line-height:1}
h3{font-family:"PT Sans Narrow",sans-serif;font-weight:700;font-size:22px;color:var(--heading);line-height:1}
.body{font-size:12.4px;font-weight:400;line-height:15.6px;text-align:justify;color:#5a5a5a}
.q{position:absolute;left:0;width:517px;font-size:12.8px;font-weight:400;line-height:15.6px;padding-left:35px;color:#5a5a5a}
.num{position:absolute;left:0;width:23px;height:23px;border:1px solid #777;border-radius:50%;text-align:center;line-height:21px;font-size:11px;font-weight:300}
.news{position:absolute;left:0;width:274px;height:60px}
.date{position:absolute;left:0;top:0;width:57px;height:57px;border:1px solid #555;border-radius:50%;text-align:center;font-weight:300;color:var(--heading)}
.date b{display:block;font-weight:300;font-size:21px;line-height:20px;margin-top:10px}
.date span{font-size:12px}
.news h4{position:absolute;left:67px;top:0;font-size:12.5px;font-weight:400;color:var(--heading)}
.news p{position:absolute;left:67px;top:22px;width:207px;font-size:12px;font-weight:400;line-height:15.6px;text-align:justify;color:#5a5a5a}
.panel{position:absolute;left:0;width:274px;height:42px;background:var(--panel);font-size:13px;font-weight:400;line-height:42px;color:#444}
.panel .num{top:10px;left:8px;background:transparent}
.panel.numbered{padding-left:41px}
.panel.arrowed{padding-left:30px}
.panel.arrowed::before{content:"\2192";position:absolute;left:14px;font-size:8px;font-weight:600}

/* footer */
.site-footer{position:absolute;left:0;top:1025px;width:1040px;height:175px;background:var(--footer-bg);color:#e6e6e6}
.site-footer h3{color:var(--white);position:absolute;top:32px;font-size:20px}
.links{position:absolute;left:106px;top:64px;list-style:none;font-size:13px;line-height:15.6px;font-weight:300}
.contact{position:absolute;left:271px;top:64px;font-size:13px;line-height:15.6px;font-weight:300}
.email-field{position:absolute;left:521px;top:68px;width:217px;height:34px;background:var(--white);border:1px solid #ccc;border-radius:2px;font-size:11px;font-style:italic;color:#555;line-height:32px;padding-left:46px}
.email-field svg{position:absolute;left:10px;top:7px}
.nl-note{position:absolute;left:525px;top:109px;width:210px;font-size:11px;font-style:italic;line-height:12.2px;font-weight:300}
.social{position:absolute;top:66px;width:39px;height:39px;border-radius:50%}
.copy{position:absolute;left:773px;top:137px;font-size:11.5px;font-weight:300}
</style>
</head>
<body>

<header class="site-header">
  <div class="brand">Speech, Thought and Nerve Lab</div>
  <nav class="nav">
    <a class="active" style="left:380px">Home</a>
    <a style="left:471px">People</a>
    <a style="left:552px">Publications</a>
    <a style="left:670px">Research</a>
    <a style="left:765px">Blog</a>
    <a style="left:829px">Codebase</a>
  </nav>
</header>

<section class="hero" role="img" aria-label="Glowing blue DNA double helix with floating particles">
  <div class="welcome">
    <h1>WELCOME TO THE LAB</h1>
    <p>Language is a complex mental faculty, recruiting and integrating several interacting representational and computational architectures in the mind. At the Speech, Thought and Nerve Lab (SoTeN Lab</p>
    <div class="btn">Learn More</div>
  </div>
  <div class="slider-nav">
    <svg width="50" height="35" viewBox="0 0 50 35"><path d="M22 9 L15 17.5 L22 26 M28 9 L35 17.5 L28 26" fill="none" stroke="#fff" stroke-width="1.6"/></svg>
  </div>
  <div class="hero-tag">Speech, Thought and Nerve Lab</div>
</section>

<main>
  <section class="abs" style="left:111px;top:507px;width:517px">
    <h2 class="big">THE LAB</h2>
    <p class="body" style="margin-top:13px">Language is a complex mental faculty, recruiting and integrating several interacting representational and computational architectures in the mind. At the Speech, Thought and Nerve Lab (SoTeN Lab), we investigate the nature of the cognitive and neural architecture that supports the human language system and how it interfaces with other cognitive faculties. We combine insights from linguistic theory, processing models and what is known about their neurobiological underpinnings in order to guide our research questions</p>
  </section>

  <section class="abs" style="left:111px;top:665px;width:517px;height:160px">
    <h3>The core questions</h3>
    <div class="q" style="top:44px"><span class="num" style="top:-3px">1</span>What is the nature of linguistic representations?</div>
    <div class="q" style="top:75px;padding-right:12px"><span class="num" style="top:4px">2</span>How are these representations recruited and deployed in real-time language comprehension and production?</div>
    <div class="q" style="top:122px;padding-right:12px;text-align:justify"><span class="num" style="top:2px">3</span>What is the neural architecture underlying these representations and computational processes?</div>
  </section>

  <section class="abs" style="left:111px;top:839px;width:518px">
    <h3>The research methods</h3>
    <p class="body" style="margin-top:5px">The lab houses several behavioral testing stations, as well as a 128-channel EEG system (SignalAmp DC, by NeuroWare, Germany). The lab is also affiliated with the Cortical Speech Unit, which houses a state-of-the-art 208-channel whole-head MEG system (by the Northvale Institute of Technology, Japan), allowing for unimodal MEG recordings as well as concurrent EEG-MEG recordings with up to 64 EEG channels. In addition, a state-of-the-art fMRI facility is currently under construction in the new Harbor University campus in Pearl Island, which will expand the repertoire of brain imaging research that can be carried out in the lab.</p>
  </section>

  <aside class="abs" style="left:653px;top:502px;width:274px;height:520px">
    <h3 style="position:absolute;top:0">Latest News</h3>
    <div class="news" style="top:35px">
      <div class="date"><b>01</b><span>OCT</span></div>
      <h4>Lab website is up and running!</h4>
      <p>Eusus consequam vitae habitur amet nullam vitae condis phasellus sed justo.</p>
    </div>
    <div class="news" style="top:114px">
      <div class="date"><b>12</b><span>OCT</span></div>
      <h4>Lab website is up and running!</h4>
      <p>Eusus consequam vitae habitur amet nullam vitae condis phasellus sed justo.</p>
    </div>
    <h3 style="position:absolute;top:195px">Current lab experiments</h3>
    <div class="panel numbered" style="top:234px"><span class="num">1</span>Speech sounds</div>
    <div class="panel numbered" style="top:279px"><span class="num">2</span>Sentence comprehension in English</div>
    <h3 style="position:absolute;top:338px">Current lab experiments</h3>
    <div class="panel arrowed" style="top:374px">Words in Hebrew</div>
    <div class="panel arrowed" style="top:420px">Survey of Modern Standard Arabic Words</div>
    <div class="panel arrowed" style="top:467px">Reading sentences in English</div>
  </aside>
</main>

<footer class="site-footer">
  <h3 style="left:103px">Quick Links</h3>
  <ul class="links">
    <li>Home</li><li>People</li><li>Publications</li><li>Research</li><li>Blog</li><li>Codebase</li>
  </ul>
  <h3 style="left:269px">Contact Address</h3>
  <div class="contact">
    <div>Address : 48 Cedar Court,</div>
    <div style="padding-left:54px">Port Alder,</div>
    <div style="padding-left:54px">P.O. Box 50213,</div>
    <div style="padding-left:54px">Westland Republic</div>
    <div>Email &nbsp;&nbsp;&nbsp;: soten.lab@example.org</div>
  </div>
  <h3 style="left:521px">Newsletter</h3>
  <div class="email-field">
    <svg width="22" height="18" viewBox="0 0 22 18"><rect x="1" y="3" width="20" height="14" fill="#f2c66b" stroke="#c99a3a"/><path d="M1 3 L11 11 L21 3" fill="none" stroke="#c99a3a"/></svg>
    Enter your Email id
  </div>
  <p class="nl-note">Sed ut perspiciatis unde omnis iste natus error sit voluptatem accusantium doloremque laudantium,</p>
  <h3 style="left:773px">Follow Us</h3>
  <span class="social" style="left:772px;background:var(--social-1)"></span>
  <span class="social" style="left:815px;background:var(--social-2)"></span>
  <span class="social" style="left:858px;background:var(--social-3)"></span>
  <div class="copy">©2014.www.soten-lab.example</div>
</footer>

</body>
</html>
```